Business Card Design Project

Industry/Entity Type

Business

Contact Information for Business Card

The Mercy Hill Gospel Choir
Dean Farrow, Minister of Music

The Harvest Covenant Church of Greenfield
Founded 1868

Blinkr @themhgc
Picturo mercyhillgc
Friendwall friendwall.example/mhgc408
Website: mercyhillgc.example
For Bookings: (555) 552-MHGC
4827 Marlowe Avenue, Millbrook, OH 44720

Back of the Card
Music and Cd's Recordings Available On
Choirs Website and Also
Tunevault, Orbita Music, Disc Pony (the music online logo)

```html
<!DOCTYPE html>
<html lang="en">
<head>
<meta charset="utf-8">
<title>The Mercy Hill Gospel Choir – Business Card</title>
<link rel="stylesheet" href="https://fonts.googleapis.com/css2?family=Cinzel:wght@600&family=Roboto:wght@400;500&family=Pinyon+Script&family=Tinos&display=swap">
<style>
  :root {
    --stage: #e7e2d9;
    --green-light: #285a2e;
    --green-dark: #0e2a15;
    --gold: #d9b653;
    --gold-light: #f4e39a;
    --gold-deep: #a9812a;
    --ink-green: #1d3b22;
    --text-light: #f1f1ee;
  }
  html, body { margin: 0; padding: 0; overflow: hidden; }
  body { width: 900px; height: 1200px; background: var(--stage); position: relative; }

  .card {
    position: absolute; left: 82px; width: 733px; height: 428px;
    border-radius: 22px; overflow: hidden;
    background: radial-gradient(ellipse at 45% 25%, var(--green-light), var(--green-dark) 80%);
    box-shadow: 0 8px 18px rgba(0,0,0,.25);
  }
  .card--front { top: 138px; }
  .card--back { top: 633px; }
  .card-art { position: absolute; inset: 0; }

  .choir-title {
    position: absolute; margin: 0; font-family: "Cinzel", serif; font-weight: 600;
    color: var(--gold); line-height: 1; white-space: nowrap;
  }
  .choir-title .main { display: block; font-size: 37px; }
  .choir-title .sub { display: flex; align-items: center; gap: 8px; font-size: 26px; margin-top: 10px; }
  .choir-title .sub::before, .choir-title .sub::after { content: ""; height: 2px; width: 40px; background: var(--gold); }
  .card--front .choir-title { left: 38px; top: 36px; }
  .card--back .choir-title { left: 0; right: 0; top: 163px; text-align: center; }
  .card--back .choir-title .sub { justify-content: center; }

  .person-name { position: absolute; left: 38px; top: 124px; margin: 0; font: 500 27px "Roboto", sans-serif; color: var(--text-light); }
  .person-role { position: absolute; left: 38px; top: 160px; margin: 0; font: 24px "Pinyon Script", cursive; color: var(--text-light); }

  .client-mark { position: absolute; display: flex; flex-direction: column; align-items: center; gap: 5px; }
  .client-mark .dot { border-radius: 50%; background: var(--gold); }
  .client-mark span { font: 500 15px "Roboto", sans-serif; color: var(--gold); white-space: nowrap; }
  .card--front .client-mark { left: 545px; top: 26px; width: 110px; }
  .card--front .client-mark .dot { width: 84px; height: 84px; }
  .card--back .client-mark { left: 316px; top: 48px; width: 100px; }
  .card--back .client-mark .dot { width: 68px; height: 68px; }

  .contact { position: absolute; left: 38px; top: 284px; font-family: "Roboto", sans-serif; color: var(--ink-green); }
  .contact p { margin: 0 0 9px; font-size: 17px; }
  .contact .bookings { font-size: 20px; font-weight: 500; margin-bottom: 7px; }

  .socials { position: absolute; right: 20px; top: 231px; list-style: none; margin: 0; padding: 0; }
  .socials li { display: flex; align-items: center; justify-content: flex-end; gap: 10px; height: 34px; font: 17px "Roboto", sans-serif; color: var(--ink-green); }
  .socials .dot { width: 28px; height: 28px; border-radius: 50%; background: var(--ink-green); border: 2px solid var(--gold-light); box-sizing: border-box; }

  .church-line { position: absolute; left: 0; right: 0; top: 395px; margin: 0; text-align: center; font: 18px "Roboto", sans-serif; color: var(--text-light); }

  .availability { position: absolute; left: 0; right: 0; top: 254px; margin: 0; text-align: center; font: 18px/26px "Tinos", serif; color: var(--text-light); }
  .stores { position: absolute; left: 0; right: 0; top: 330px; display: flex; justify-content: center; gap: 46px; margin: 0; padding: 0; list-style: none; }
  .stores li { font: 500 29px "Roboto", sans-serif; color: var(--gold); }
</style>
</head>
<body>

<section class="card card--front">
  <svg class="card-art" width="733" height="428" viewBox="0 0 733 428">
    <defs>
      <linearGradient id="goldSweep" x1="0" y1="0" x2="1" y2="0">
        <stop offset="0" stop-color="var(--gold-deep)"/>
        <stop offset=".35" stop-color="var(--gold-light)"/>
        <stop offset=".7" stop-color="var(--gold)"/>
        <stop offset="1" stop-color="var(--gold-light)"/>
      </linearGradient>
    </defs>
    <path d="M0 192 Q360 230 733 142 L733 156 Q360 250 0 214 Z" fill="url(#goldSweep)"/>
    <path d="M0 238 Q380 290 733 170 L733 340 Q380 405 0 385 Z" fill="url(#goldSweep)"/>
    <path d="M0 368 Q380 392 733 326 L733 334 Q380 402 0 376 Z" fill="var(--gold-deep)" opacity=".6"/>
  </svg>

  <h1 class="choir-title"><span class="main">THE MERCY HILL</span><span class="sub">GOSPEL CHOIR</span></h1>
  <p class="person-name">Dean Farrow</p>
  <p class="person-role">Minister of Music</p>

  <div class="client-mark" role="img" aria-label="Mercy Hill Gospel Choir crest">
    <div class="dot"></div><span>Mercy Hill</span>
  </div>

  <div class="contact">
    <p class="bookings">For Bookings: (555) 552-MHGC</p>
    <p>www.mercyhillgc.example</p>
    <p>4827 Marlowe Avenue, Millbrook, OH 44720</p>
  </div>

  <ul class="socials">
    <li aria-label="Blinkr">@themhgc <span class="dot"></span></li>
    <li aria-label="Picturo">mercyhillgc <span class="dot"></span></li>
    <li aria-label="Friendwall">mhgc408 <span class="dot"></span></li>
  </ul>

  <p class="church-line">The Harvest Covenant Church of Greenfield &nbsp;/ Founded 1868</p>
</section>

<section class="card card--back">
  <svg class="card-art" width="733" height="428" viewBox="0 0 733 428">
    <defs>
      <linearGradient id="goldBar" x1="0" y1="0" x2="1" y2="0">
        <stop offset="0" stop-color="var(--gold-deep)"/>
        <stop offset=".4" stop-color="var(--gold-light)"/>
        <stop offset="1" stop-color="var(--gold)"/>
      </linearGradient>
    </defs>
    <rect x="0" y="412" width="733" height="16" fill="url(#goldBar)"/>
  </svg>

  <div class="client-mark" role="img" aria-label="Mercy Hill Gospel Choir crest">
    <div class="dot"></div><span>Mercy Hill</span>
  </div>

  <h2 class="choir-title"><span class="main">THE MERCY HILL</span><span class="sub">GOSPEL CHOIR</span></h2>

  <p class="availability">Music and Cd's Recordings Available On<br>Choirs Website and Also</p>

  <ul class="stores">
    <li>Tunevault</li>
    <li>Orbita Music</li>
    <li>Disc Pony</li>
  </ul>
</section>

</body>
</html>
```